Software Specialist in Artificial Intelligence innovation needs a smart and professional looking bus

Prefers a clean and professional design, yet portraying a class of its own and a world-class feel. We develop state-of-the-art software automation engines by deploying artificial intelligence that simulates the smartest brains that are able to simulate a human consultant and/or data scientist. Both single-sided or double-sided design is acceptable. Do not refer too much to our current website as we are also in the process of revamping it so that it better reflects who we are and what we do.
Updates

Project Deadline Extended
Reason: A substantial number of designs submitted to date deviates a fair bit from requirements and expectations. Feedbacks will be provided to all parties by today and as such, an extension is catered to accomodate re-submissions.

Target Market(s)

Software technology companies, software developers, enterprise clients that requires automation supported by Artificial Intelligence driven software solutions.

Industry/Entity Type

Software

Contact Information for Business Card

Marlo Vance
Chief Innovator
marlovance@brightquill.example
mobile: +65 94417302
Company Name: BrightQuill Pte Ltd
Address: 14 Tessaly Road #03-11 Harrow Court, Singapore 539204
Telephone: +65 63175420
Website: www.BrightQuill.example
Please do not include the titles of the above fields.

Font styles to use
Sans Serif
Other font styles liked:
• Calibri, Futura Condensed

Requirements
Must have
• Portrays a professional and innovative image. Should reflect that the company is into Artificial Intelligence software development, high tech kind of feel.
Nice to have
• A plus point would be if you can even come up with a new company logo for us, representing who we are. Our current company logo is attached.
Should not have
• Fanciful stuffs as it must portray a professional image. Prefers not to have the cloud "image" as part of the logo or in the name card.

```html
<!DOCTYPE html>
<html lang="en">
<head>
<meta charset="utf-8">
<title>BrightQuill Business Card</title>
<link rel="stylesheet" href="https://fonts.googleapis.com/css2?family=Open+Sans:wght@400;600;700&display=swap">
<style>
  :root {
    --bg: #ededee;
    --card-white: #ffffff;
    --card-grey: #a6a5a9;
    --charcoal: #444446;
    --brand-red: #a51d25;
    --text-light: #f2f2f2;
    --text-muted: #d9d9db;
  }
  * { margin: 0; padding: 0; box-sizing: border-box; }
  html, body { width: 1200px; height: 720px; overflow: hidden; }
  body {
    background: var(--bg);
    font-family: "Open Sans", sans-serif;
    position: relative;
  }
  .card {
    position: absolute;
    top: 212px;
    width: 520px;
    height: 297px;
    overflow: hidden;
    box-shadow: 0 2px 6px rgba(0,0,0,0.12);
  }
  /* Back side */
  .card-back {
    left: 50px;
    background: var(--card-grey);
  }
  .card-back .company-block {
    position: absolute;
    left: 0; right: 0; top: 104px;
    text-align: center;
  }
  .card-back .company-name {
    font-size: 24px;
    font-weight: 700;
    color: var(--card-white);
    letter-spacing: 0.2px;
  }
  .card-back .tagline {
    margin-top: 4px;
    font-size: 13px;
    color: var(--card-white);
  }
  .card-back .website {
    margin-top: 14px;
    font-size: 13px;
    font-weight: 600;
    color: var(--brand-red);
  }
  /* Front side */
  .card-front {
    left: 630px;
    background: var(--card-white);
  }
  .card-front .panel {
    position: absolute;
    inset: 0;
    width: 520px;
    height: 297px;
  }
  .wordmark {
    position: absolute;
    left: 34px;
    top: 64px;
    display: flex;
    align-items: center;
    gap: 8px;
  }
  .wordmark .mark-square {
    width: 18px; height: 18px;
    background: var(--brand-red);
  }
  .wordmark .mark-name {
    font-size: 21px;
    font-weight: 400;
    color: var(--brand-red);
  }
  .identity {
    position: absolute;
    right: 26px;
    top: 76px;
    text-align: right;
    color: var(--text-light);
  }
  .identity .person-name { font-size: 19px; font-weight: 400; }
  .identity .person-title { font-size: 12px; color: var(--text-muted); }
  .contact-list {
    position: absolute;
    right: 20px;
    top: 150px;
    list-style: none;
    text-align: right;
    color: var(--text-light);
    font-size: 11.5px;
    line-height: 19px;
  }
  .contact-list li {
    display: flex;
    justify-content: flex-end;
    align-items: center;
    gap: 8px;
  }
  .contact-list .icon { width: 12px; height: 12px; flex: none; }
  .contact-list .address-line2 { padding-right: 20px; line-height: 15px; }
  .contact-list strong { font-weight: 700; }
</style>
</head>
<body>

  <section class="card card-back" aria-label="Business card, back">
    <div class="company-block">
      <p class="company-name">BrightQuill Pte Ltd</p>
      <p class="tagline">Powering The New Business Paradigm</p>
      <p class="website">www.BrightQuill.example</p>
    </div>
  </section>

  <section class="card card-front" aria-label="Business card, front">
    <svg class="panel" viewBox="0 0 520 297" aria-hidden="true">
      <path d="M296 0 L340 0 Q 270 140 318 297 L 300 297 Q 255 140 296 0 Z" fill="var(--brand-red)"/>
      <path d="M340 0 L520 0 L520 297 L318 297 Q 270 140 340 0 Z" fill="var(--charcoal)"/>
    </svg>

    <div class="wordmark">
      <span class="mark-square"></span>
      <span class="mark-name">BrightQuill</span>
    </div>

    <div class="identity">
      <p class="person-name">Marlo Vance</p>
      <p class="person-title">Chief Innovator Officer</p>
    </div>

    <ul class="contact-list">
      <li>marlovance@brightquill.example
        <svg class="icon" viewBox="0 0 12 12" aria-label="email"><rect x="0.5" y="2.5" width="11" height="7" fill="none" stroke="#ddd"/><path d="M0.5 2.5 L6 7 L11.5 2.5" fill="none" stroke="#ddd"/></svg>
      </li>
      <li>+65 9441 7302
        <svg class="icon" viewBox="0 0 12 12" aria-label="mobile"><rect x="3" y="0.5" width="6" height="11" rx="1" fill="none" stroke="#ddd"/><rect x="4.5" y="2" width="3" height="5" fill="#ddd"/></svg>
      </li>
      <li>+65 6317 5420
        <svg class="icon" viewBox="0 0 12 12" aria-label="telephone"><path d="M1 4 Q6 0 11 4 L9.5 5.5 L8 4.5 L4 4.5 L2.5 5.5 Z" fill="#ddd"/><rect x="2.5" y="6" width="7" height="5" rx="1" fill="#ddd"/></svg>
      </li>
      <li><span><strong>14 Tessaly Road</strong> #03-11</span>
        <svg class="icon" viewBox="0 0 12 12" aria-label="location"><path d="M6 11.5 L2.5 6 A4 4 0 1 1 9.5 6 Z" fill="#ddd"/><circle cx="6" cy="4.5" r="1.4" fill="var(--charcoal)"/></svg>
      </li>
      <li class="address-line2">Singapore 539204</li>
    </ul>
  </section>

</body>
</html>
```